Harbor Lawn and Stoneworks Flyer/Brochure

Flyer/Brochure for artificial turf and paver company. Photos and txt<br/>Specializes in Turf, Pavers, Patio, Decorative Rock, Hardscape, Landscape Design.

Target Market(s)

Homeowners

Industry/Entity Type

Construction

Font styles to use
Sans Serif

Colors
9bcb3c

Requirements
Must have
• Photos, we will provide as well as logo
• phone number and email address
• similar branding as website
• www.harborlsw.com
Nice to have
• eye catching not too busy
• clean and easy to read
• Hi! Please see photos on our instagram - there are a couple shots that may be better than the website there.
• Also, photo of dog on turf. Please mention kid -play turf and pet turf is available or something like "your pup will love our pet turf"
• Add- "Ask us about our specials"
• phone number is 800-413-2786

```html
<!DOCTYPE html>
<html lang="en">
<head>
<meta charset="utf-8">
<title>Harbor Lawn and Stoneworks Flyer</title>
<link href="https://fonts.googleapis.com/css2?family=Anton&family=Montserrat:wght@400;600;800&display=swap" rel="stylesheet">
<style>
  :root {
    --brand-green: #9bcb3c;
    --deep-green: #6fa62a;
    --charcoal: #2c2c2e;
    --charcoal-light: #3a3a3d;
    --ink: #161616;
    --white: #ffffff;
    --stage: #d9d9d6;
  }
  * { margin: 0; padding: 0; box-sizing: border-box; }
  html, body { width: 1200px; height: 800px; overflow: hidden; background: var(--stage); }
  .canvas { position: relative; width: 1200px; height: 800px; }
  .flyer {
    position: absolute; left: 315px; top: 20px; width: 570px; height: 760px;
    overflow: hidden; background: var(--charcoal);
    font-family: "Montserrat", sans-serif; color: var(--white);
    box-shadow: 0 6px 24px rgba(0,0,0,.25);
  }
  .flyer-shapes { position: absolute; inset: 0; }
  .brand {
    position: absolute; top: 34px; left: 0; right: 0; text-align: center;
  }
  .brand-name {
    font-family: "Montserrat", sans-serif; font-weight: 800; font-size: 30px;
    letter-spacing: 1px; color: var(--white); text-transform: uppercase; line-height: 1.05;
  }
  .brand-tag {
    margin-top: 8px; font-size: 13px; font-weight: 600; letter-spacing: 3px;
    color: var(--white); text-transform: uppercase;
  }
  .brand-tag::before, .brand-tag::after {
    content: ""; display: inline-block; width: 26px; height: 3px;
    background: var(--brand-green); vertical-align: middle; margin: 0 10px;
  }
  .headline {
    position: absolute; top: 160px; left: 0; right: 0; text-align: center;
    font-family: "Anton", sans-serif; color: var(--ink); text-transform: uppercase; line-height: 1;
  }
  .headline-lead { font-size: 34px; }
  .headline-main { font-size: 58px; margin-top: 2px; }
  .headline-tail { font-size: 26px; letter-spacing: 9px; margin-top: 4px; }
  .headline-banner {
    display: inline-block; margin-top: 8px; padding: 5px 22px;
    background: var(--brand-green); color: var(--white);
    font-family: "Montserrat", sans-serif; font-weight: 600; font-size: 14px; letter-spacing: 1.5px;
  }
  .services-title {
    position: absolute; top: 468px; left: 0; right: 0; text-align: center;
    font-family: "Anton", sans-serif; text-transform: uppercase; line-height: 1;
  }
  .services-title-main { font-size: 44px; color: var(--brand-green); }
  .services-title-sub { font-size: 22px; color: var(--white); margin-top: 4px; letter-spacing: 1px; }
  .service-list {
    position: absolute; top: 560px; left: 20px; right: 20px;
    display: flex; justify-content: space-between; list-style: none;
  }
  .service { width: 84px; text-align: center; font-size: 13px; color: var(--white); }
  .service svg { display: block; margin: 0 auto 6px; width: 40px; height: 40px; }
  .contact {
    position: absolute; top: 672px; left: 0; right: 0; text-align: center; color: var(--white);
  }
  .contact-specials { font-family: "Anton", sans-serif; font-size: 20px; letter-spacing: .5px; }
  .contact-phone { font-family: "Anton", sans-serif; font-size: 22px; margin-top: 2px; }
  .contact-line { font-size: 11px; margin-top: 3px; }
</style>
</head>
<body>
<div class="canvas">
  <article class="flyer">
    <svg class="flyer-shapes" viewBox="0 0 570 760" width="570" height="760" aria-hidden="false">
      <defs>
        <linearGradient id="photoTone" x1="0" y1="0" x2="0" y2="1">
          <stop offset="0" stop-color="#4b5a2c"/>
          <stop offset=".45" stop-color="#8c9a52"/>
          <stop offset=".7" stop-color="#6f8a3a"/>
          <stop offset="1" stop-color="#4f7a24"/>
        </linearGradient>
      </defs>
      <rect width="570" height="760" fill="var(--charcoal)"/>
      <path d="M0 0 H570 V400 Q300 470 0 410 Z" fill="url(#photoTone)" role="img" aria-label="Photo of a child running across a wide green turf field under a stormy sky"/>
      <path d="M0 410 Q300 470 570 400 V416 Q300 492 0 422 Z" fill="var(--white)"/>
      <path d="M0 640 Q260 585 570 692 V760 H0 Z" fill="var(--white)"/>
      <path d="M0 654 Q260 602 570 704 V760 H0 Z" fill="var(--brand-green)"/>
    </svg>

    <header class="brand">
      <div class="brand-name">Harbor Lawn</div>
      <div class="brand-tag">and Stoneworks</div>
    </header>

    <h1 class="headline">
      <div class="headline-lead">Make your</div>
      <div class="headline-main">Outdoor Living</div>
      <div class="headline-tail">Vision a Reality</div>
      <div class="headline-banner">YOUR PUP WILL LOVE OUR PET TURF</div>
    </h1>

    <h2 class="services-title">
      <div class="services-title-main">Specializes</div>
      <div class="services-title-sub">For our outdoor living</div>
    </h2>

    <ul class="service-list">
      <li class="service">
        <svg viewBox="0 0 40 40" fill="var(--brand-green)"><path d="M4 36 L10 12 L13 36 Z M12 36 L18 6 L22 36 Z M20 36 L27 10 L29 36 Z M28 36 L36 16 L36 36 Z"/></svg>
        Turf
      </li>
      <li class="service">
        <svg viewBox="0 0 40 40" fill="none" stroke="var(--brand-green)" stroke-width="2.5"><rect x="4" y="8" width="14" height="10"/><rect x="22" y="8" width="14" height="10"/><rect x="4" y="22" width="8" height="10"/><rect x="15" y="22" width="21" height="10"/></svg>
        Pavers
      </li>
      <li class="service">
        <svg viewBox="0 0 40 40" fill="none" stroke="var(--brand-green)" stroke-width="2.5"><path d="M4 16 Q20 2 36 16 Z"/><line x1="20" y1="16" x2="20" y2="36"/><line x1="10" y1="28" x2="30" y2="28"/><line x1="8" y1="24" x2="8" y2="36"/><line x1="32" y1="24" x2="32" y2="36"/></svg>
        Patio
      </li>
      <li class="service">
        <svg viewBox="0 0 40 40" fill="var(--brand-green)"><ellipse cx="20" cy="32" rx="15" ry="5"/><ellipse cx="20" cy="22" rx="11" ry="4.5"/><ellipse cx="20" cy="13" rx="7" ry="3.5"/><ellipse cx="20" cy="6" rx="4" ry="2.5"/></svg>
        Rock
      </li>
      <li class="service">
        <svg viewBox="0 0 40 40" fill="none" stroke="var(--brand-green)" stroke-width="2.5"><rect x="5" y="5" width="30" height="30"/><path d="M5 18 L18 5 M5 30 L30 5 M12 35 L35 12 M24 35 L35 24"/></svg>
        Hardscape
      </li>
      <li class="service">
        <svg viewBox="0 0 40 40" fill="none" stroke="var(--brand-green)" stroke-width="2.5"><path d="M4 34 Q20 22 36 34"/><line x1="20" y1="30" x2="20" y2="12"/><path d="M20 18 Q10 16 10 6 Q20 8 20 18 Z"/><path d="M20 14 Q28 12 30 4 Q21 5 20 14 Z"/></svg>
        Landscape
      </li>
    </ul>

    <footer class="contact">
      <div class="contact-specials">Ask Us About Our Specials</div>
      <div class="contact-phone">800-413-2786</div>
      <div class="contact-line">info@harborlsw.com &nbsp;|&nbsp; www.harborlsw.com</div>
      <div class="contact-line">2750 W Marlow Ave, Brea, CA 92821, USA</div>
    </footer>
  </article>
</div>
</body>
</html>
```